Tampa, Florida based Real Estate company Business Cards

Need ideas for real estate business cards
Updates

Need extra days to review

Industry/Entity Type

Real Estate

Contact Information for Business Card

Space for image, space for logo, contact information space

Font styles to use
Sans Serif

Colors

Designer to choose colors to be used in the design.

Requirements
Must have
• Options to have duplicate content on the back of card for a team of agents.

```html
<!DOCTYPE html>
<html lang="en">
<head>
<meta charset="utf-8">
<title>Harborline Realty – Business Cards</title>
<link href="https://fonts.googleapis.com/css2?family=Arimo:wght@400;700&display=swap" rel="stylesheet">
<style>
  :root {
    --page-bg: #ececec;
    --card-bg: #bdbdbd;
    --card-bg-light: #c6c6c6;
    --navy: #1f2463;
    --white: #ffffff;
    --soft-white: rgba(255, 255, 255, 0.85);
    --silver-text: #9a9a9a;
  }
  * { box-sizing: border-box; margin: 0; padding: 0; }
  html, body {
    width: 1200px;
    height: 802px;
    overflow: hidden;
    background: var(--page-bg);
    font-family: "Arimo", Arial, sans-serif;
  }
  .sheet {
    position: relative;
    width: 1200px;
    height: 802px;
    display: flex;
    align-items: center;
    justify-content: center;
    gap: 40px;
  }
  .card {
    position: relative;
    width: 540px;
    height: 309px;
    background: linear-gradient(160deg, var(--card-bg-light), var(--card-bg));
    box-shadow: 0 6px 18px rgba(0, 0, 0, 0.18);
    overflow: hidden;
  }

  /* Front */
  .brand-name {
    position: absolute;
    top: 58px;
    right: 40px;
    font-size: 34px;
    font-weight: 400;
    letter-spacing: 2px;
    color: var(--navy);
    text-transform: uppercase;
    text-align: right;
    line-height: 1;
  }
  .divider {
    position: absolute;
    left: 30px;
    right: 30px;
    top: 150px;
    height: 1px;
    background: var(--soft-white);
  }
  .address {
    position: absolute;
    top: 166px;
    right: 40px;
    text-align: right;
    font-size: 13px;
    line-height: 1.35;
    color: var(--white);
  }
  .person {
    position: absolute;
    left: 34px;
    bottom: 30px;
  }
  .person-name {
    font-size: 15px;
    font-weight: 700;
    color: var(--navy);
    text-transform: uppercase;
    letter-spacing: 0.3px;
  }
  .person-role {
    font-size: 13px;
    color: var(--white);
    margin: 2px 0 10px;
  }
  .contact-list { list-style: none; }
  .contact-item {
    display: flex;
    align-items: center;
    gap: 8px;
    font-size: 13px;
    line-height: 1.45;
    color: var(--white);
  }
  .contact-icon { width: 11px; height: 11px; flex: none; }

  /* Back */
  .card--back .brand-name-embossed {
    position: absolute;
    inset: 0;
    display: flex;
    align-items: center;
    justify-content: center;
    font-size: 38px;
    font-weight: 400;
    letter-spacing: 3px;
    text-transform: uppercase;
    color: var(--silver-text);
    white-space: nowrap;
  }
</style>
</head>
<body>
<main class="sheet">

  <section class="card card--front" aria-label="Business card front">
    <div class="brand-name">Harborline<br>Realty</div>
    <div class="divider"></div>
    <p class="address">Your address, city<br>state, ZIP 0000</p>

    <div class="person">
      <p class="person-name">Daniel Reyes</p>
      <p class="person-role">Manager</p>
      <ul class="contact-list">
        <li class="contact-item">
          <svg class="contact-icon" viewBox="0 0 12 12" aria-hidden="true"><path fill="#1f2463" d="M2.5 1l2 2.2-1 1.3c.7 1.6 1.8 2.7 3.4 3.4l1.3-1L10.5 9 9.3 11C5 10.6 1.4 7 1 2.7z"/></svg>
          555-018-7342
        </li>
        <li class="contact-item">
          <svg class="contact-icon" viewBox="0 0 12 12" aria-hidden="true"><rect x="1" y="2.5" width="10" height="7" fill="none" stroke="#1f2463" stroke-width="1.1"/><path d="M1 2.8l5 4 5-4" fill="none" stroke="#1f2463" stroke-width="1.1"/></svg>
          youremail@example.com
        </li>
        <li class="contact-item">
          <svg class="contact-icon" viewBox="0 0 12 12" aria-hidden="true"><circle cx="6" cy="6" r="5" fill="#1f2463"/><path d="M1 6h10M6 1c-2 2.5-2 7.5 0 10M6 1c2 2.5 2 7.5 0 10" fill="none" stroke="#c6c6c6" stroke-width="0.7"/></svg>
          www.yourwebsite.com
        </li>
      </ul>
    </div>
  </section>

  <section class="card card--back" aria-label="Business card back">
    <div class="brand-name-embossed">Harborline Realty</div>
  </section>

</main>
</body>
</html>
```